Brightwater Dental
Stationary for Pediatric Dental & Orthodontics - Health
Stationary for Pediatric Dental & Orthodontics
Bright & Fun-filled
Pediatrics & Orthodontics
Larkspur Hollow Prof. Center 48517 Larkspur Hollow Ave. Suite B-07 Gaithersburg, MD 20886
info@brightwaterdental.org
www.brightwaterdental.org
I have uploaded the co logo to use for the card. I am looking for biz card (2 sided), appointment card, rewards biz card (can explain later, but basically the biz card with an offer on the back), referral pad, envelope (1 sided-no flap work), letterhead, & folder. I would also like to have a QR code linked to the company website on all materials, if it can be color and still work that would be great. I uploaded the static code that I have currently.
This only needs to be on the back of the biz card not the other materials........... Helping Children Who Need: Fillings, Braces, Crowns, Laughing Gas, Whitening, Mouthguards, Hospital Care, Special Needs Care, Clearvane, Nightguards, Cosmetics, Extractions, Walk-in Emergencies, Dental Home.................... Carewell and Most Insurances Accepted

```html
<!DOCTYPE html>
<html lang="en">
<head>
<meta charset="utf-8">
<title>Brightwater Dental – Business Card</title>
<link rel="stylesheet" href="https://fonts.googleapis.com/css2?family=Montserrat:wght@300;400;600&display=swap">
<style>
  :root{
    --page:#eceae6;
    --card:#ffffff;
    --blue:#2f6db5;
    --green:#6cbd45;
    --ink:#2b2b2b;
    --muted:#5a5a5a;
    --on-blue:#ffffff;
  }
  html,body{margin:0;padding:0;width:1200px;height:1086px;overflow:hidden;background:var(--page);}
  body{display:flex;align-items:center;justify-content:center;font-family:"Montserrat",sans-serif;}
  .card{position:relative;width:1000px;height:571px;background:var(--card);box-shadow:0 8px 30px rgba(0,0,0,.18);overflow:hidden;}
  .contact-panel{position:absolute;left:0;top:0;width:470px;height:571px;}
  .contact-list{position:absolute;left:0;top:0;width:470px;height:571px;margin:0;padding:0;list-style:none;}
  .contact-row{position:absolute;left:40px;width:320px;text-align:right;color:var(--on-blue);font-size:21px;font-weight:400;line-height:1.4;letter-spacing:.5px;}
  .contact-row.phone{top:100px;}
  .contact-row.address{top:232px;font-size:19px;}
  .contact-row.web{top:392px;font-size:19px;}
  .icon{position:absolute;left:378px;width:64px;height:64px;}
  .icon.phone{top:108px;}
  .icon.pin{top:253px;}
  .icon.globe{top:398px;}
  .brand{position:absolute;left:560px;top:170px;display:flex;align-items:center;gap:14px;}
  .brand-dot{width:34px;height:34px;border-radius:50%;background:var(--blue);}
  .brand-name{font-size:36px;font-weight:600;color:var(--blue);letter-spacing:.5px;}
  .brand-tag{position:absolute;left:608px;top:222px;font-size:14px;color:var(--green);letter-spacing:2px;text-transform:uppercase;}
  .person{position:absolute;left:560px;top:330px;}
  .person-name{margin:0;font-size:30px;font-weight:400;letter-spacing:3px;text-transform:uppercase;color:var(--ink);}
  .person-title{margin:6px 0 0;font-size:22px;font-weight:300;color:var(--muted);letter-spacing:1px;}
</style>
</head>
<body>
  <article class="card">
    <svg class="contact-panel" viewBox="0 0 470 571" aria-hidden="true">
      <path fill="var(--blue)" d="M0,0 H410 V95 A45,45 0 0 1 410,185 V240 A45,45 0 0 1 410,330 V385 A45,45 0 0 1 410,475 V571 H0 Z"/>
    </svg>

    <svg class="icon phone" viewBox="0 0 64 64" aria-hidden="true">
      <circle cx="32" cy="32" r="28" fill="var(--green)" stroke="#fff" stroke-width="3"/>
      <path fill="#fff" d="M24 18c2 0 3 4 4 6 .5 1.5-1.5 3-2 4 1.5 3.5 4 6 7.5 7.5 1-.5 2.5-2.5 4-2 2 1 6 2 6 4 0 3-3 6-6 6-11 0-20-9-20-20 0-3 3-5.5 6.5-5.5z"/>
    </svg>
    <svg class="icon pin" viewBox="0 0 64 64" aria-hidden="true">
      <circle cx="32" cy="32" r="28" fill="var(--green)" stroke="#fff" stroke-width="3"/>
      <path fill="#fff" d="M32 16c-6.5 0-11 4.5-11 10.5C21 34 32 47 32 47s11-13 11-20.5C43 20.5 38.5 16 32 16zm0 15a4.5 4.5 0 1 1 0-9 4.5 4.5 0 0 1 0 9z"/>
    </svg>
    <svg class="icon globe" viewBox="0 0 64 64" aria-hidden="true">
      <circle cx="32" cy="32" r="28" fill="var(--green)" stroke="#fff" stroke-width="3"/>
      <g fill="none" stroke="#fff" stroke-width="2.2">
        <circle cx="32" cy="32" r="14"/>
        <ellipse cx="32" cy="32" rx="6" ry="14"/>
        <line x1="18" y1="32" x2="46" y2="32"/>
        <line x1="20" y1="25" x2="44" y2="25"/>
        <line x1="20" y1="39" x2="44" y2="39"/>
      </g>
    </svg>

    <ul class="contact-list">
      <li class="contact-row phone">014 627 3058<br>014 627 3058</li>
      <li class="contact-row address">48517 Larkspur Hollow Ave.<br>Suite B-07, Gaithersburg, MD</li>
      <li class="contact-row web">info@brightwaterdental.org<br>www.brightwaterdental.org</li>
    </ul>

    <div class="brand">
      <span class="brand-dot"></span>
      <span class="brand-name">Brightwater Dental</span>
    </div>
    <div class="brand-tag">Pediatrics &amp; Orthodontics</div>

    <div class="person">
      <p class="person-name">Reid Calloway</p>
      <p class="person-title">Managing Director</p>
    </div>
  </article>
</body>
</html>
```